Brindlecove Dental Partners
Modern
Tobiah Lurent, D.M.D., PLLC
17 North Kellam Road
Brindlecove, NH 03817
Emergency (603) 555-0142
brindent@quellmail.test
www.brindlecovedental.example
Please place the practice name and my name in bold letters
APPOINTMENT
FOR _______________________________
______________AT___________O'CLOCK

```html
<!DOCTYPE html>
<html lang="en">
<head>
<meta charset="utf-8">
<title>Brindlecove Dental Partners – Business Card</title>
<link href="https://fonts.googleapis.com/css2?family=Cormorant+Garamond:wght@600;700&family=Open+Sans:wght@400;600;700&display=swap" rel="stylesheet">
<style>
  :root {
    --page: #eceeef;
    --card: #ffffff;
    --green: #5aa83c;
    --green-light: #8cc63f;
    --blue: #1f4e7f;
    --blue-light: #4f86b8;
    --ink: #4a4f55;
    --muted: #8a9097;
    --rule: #b9bec4;
    --mark-tint: #dfe8ee;
  }
  * { box-sizing: border-box; margin: 0; padding: 0; }
  html, body { width: 1200px; height: 873px; overflow: hidden; }
  body {
    background: var(--page);
    font-family: "Open Sans", Arial, sans-serif;
    color: var(--ink);
    position: relative;
  }
  .card {
    position: absolute;
    width: 540px;
    height: 310px;
    background: var(--card);
    border-radius: 18px;
    overflow: hidden;
    box-shadow: 0 6px 18px rgba(0,0,0,0.10);
  }
  .card-front { left: 40px; top: 282px; }
  .card-back { left: 620px; top: 282px; }

  /* front */
  .practice-mark {
    position: absolute; left: 34px; top: 52px;
    display: flex; align-items: center; gap: 12px;
  }
  .practice-mark .dot {
    width: 34px; height: 34px; border-radius: 50%;
    background: var(--green);
  }
  .practice-mark .name {
    font-family: "Cormorant Garamond", Georgia, serif;
    font-weight: 700;
    color: var(--blue);
    font-size: 21px;
    line-height: 1.05;
    letter-spacing: 0.5px;
    text-transform: uppercase;
  }
  .doctor-name {
    position: absolute; right: 34px; top: 66px;
    font-family: "Cormorant Garamond", Georgia, serif;
    font-weight: 700;
    font-size: 15px;
    letter-spacing: 1px;
    font-variant: small-caps;
    color: var(--green);
  }
  .accent-tab {
    position: absolute; right: 0; top: 58px;
    width: 10px; height: 30px;
    background: var(--green);
  }
  .contact-list {
    position: absolute; left: 34px; top: 182px;
    list-style: none;
    font-size: 9.5px;
    line-height: 15px;
    color: var(--ink);
  }
  .contact-list li { display: flex; align-items: center; gap: 7px; }
  .contact-list svg { width: 9px; height: 9px; fill: var(--green); flex: none; }
  .band { position: absolute; left: 0; bottom: 34px; width: 540px; height: 12px; }

  /* back */
  .appointment {
    position: absolute; left: 34px; top: 34px; right: 34px;
    font-size: 10px;
  }
  .appointment h2 {
    font-size: 11px; font-weight: 700; color: var(--ink);
    margin-bottom: 14px;
  }
  .field-row { display: flex; gap: 14px; margin-bottom: 14px; align-items: flex-end; }
  .field { display: flex; align-items: flex-end; gap: 6px; }
  .field .line { border-bottom: 1px solid var(--rule); height: 12px; }
  .days { display: flex; gap: 10px; margin: 4px 0 22px; }
  .day { display: flex; align-items: center; gap: 3px; font-size: 8px; }
  .day .box { width: 13px; height: 13px; border: 1px solid var(--muted); border-radius: 2px; }
  .policy h3 { font-size: 9.5px; font-weight: 700; margin-bottom: 3px; }
  .policy p { font-size: 8px; color: var(--muted); }
  .faint-mark {
    position: absolute; right: -40px; top: -30px;
    width: 230px; height: 230px; border-radius: 50%;
    background: var(--mark-tint);
    opacity: 0.6;
  }
  .back-band {
    position: absolute; left: 0; bottom: 0; width: 100%; height: 8px;
    background: linear-gradient(90deg, var(--green) 0%, var(--green-light) 45%, var(--blue) 55%, var(--blue-light) 100%);
  }
</style>
</head>
<body>

<section class="card card-front" aria-label="Business card front">
  <div class="practice-mark">
    <span class="dot"></span>
    <span class="name">Brindlecove<br>Dental Partners</span>
  </div>
  <span class="accent-tab"></span>
  <p class="doctor-name">Tobiah Lurent, D.M.D., PLLC</p>

  <ul class="contact-list">
    <li><svg viewBox="0 0 10 10"><path d="M5 0C3 0 1.5 1.5 1.5 3.4 1.5 6 5 10 5 10s3.5-4 3.5-6.6C8.5 1.5 7 0 5 0zm0 4.8a1.4 1.4 0 110-2.8 1.4 1.4 0 010 2.8z"/></svg>17 North Kellam Road</li>
    <li><svg viewBox="0 0 10 10"><path d="M5 0C3 0 1.5 1.5 1.5 3.4 1.5 6 5 10 5 10s3.5-4 3.5-6.6C8.5 1.5 7 0 5 0zm0 4.8a1.4 1.4 0 110-2.8 1.4 1.4 0 010 2.8z"/></svg>Brindlecove, NH 03817</li>
    <li><svg viewBox="0 0 10 10"><path d="M2.2 0.5l1.6 2.2-1 1.1c.6 1.3 1.6 2.3 2.9 2.9l1.1-1 2.2 1.6-.8 2C5 9 1 5 .2 1.3z"/></svg>Emergency (603) 555-0142</li>
    <li><svg viewBox="0 0 10 10"><path d="M0 2h10v6H0zM.6 2.4L5 5.6l4.4-3.2"/></svg>brindent@quellmail.test</li>
    <li><svg viewBox="0 0 10 10"><circle cx="5" cy="5" r="4.5"/></svg>www.brindlecovedental.example</li>
  </ul>

  <svg class="band" viewBox="0 0 540 12" preserveAspectRatio="none" aria-hidden="true">
    <defs>
      <linearGradient id="bandGreen" x1="0" x2="1">
        <stop offset="0" stop-color="#8cc63f"/>
        <stop offset="1" stop-color="#5aa83c"/>
      </linearGradient>
      <linearGradient id="bandBlue" x1="0" x2="1">
        <stop offset="0" stop-color="#1f4e7f"/>
        <stop offset="1" stop-color="#6a9cc8"/>
      </linearGradient>
    </defs>
    <polygon points="0,0 232,0 226,12 0,12" fill="url(#bandGreen)"/>
    <polygon points="235,0 540,0 540,12 229,12" fill="url(#bandBlue)"/>
  </svg>
</section>

<section class="card card-back" aria-label="Appointment card back">
  <span class="faint-mark"></span>
  <div class="appointment">
    <h2>Appointment:</h2>
    <div class="field-row">
      <div class="field">Name: <span class="line" style="width:190px"></span></div>
      <div class="field">Time: <span class="line" style="width:120px"></span></div>
    </div>
    <div class="field-row">
      <div class="field">Date: <span class="line" style="width:120px"></span></div>
    </div>
    <div class="days">
      <span class="day"><span class="box"></span>Mon</span>
      <span class="day"><span class="box"></span>Tue</span>
      <span class="day"><span class="box"></span>Wed</span>
      <span class="day"><span class="box"></span>Thu</span>
      <span class="day"><span class="box"></span>Fri</span>
      <span class="day"><span class="box"></span>Sat</span>
    </div>
    <div class="policy">
      <h3>Cancellation Policy</h3>
      <p>Please give 24 hours notice to cancel, otherwise a fee will be charged.</p>
    </div>
  </div>
  <span class="back-band"></span>
</section>

</body>
</html>
```